Business and Success Coaching Business Card

Need a business card for my coaching business. I coach small businesses, career professionals and, individuals wanting to unlock their human potential and achieve excellence. At the heart of our methodology is the Shaping Purposeful Action Routines Knowingly (SPARK) approach to formulate empowerment, create principles for success and setting achievable outcomes. I would like something that incorporates our new logo, something clean and sharp with a solid darker, but complementary background, color on the card front. The back should be white where there will be room for three questions

Target Market(s)

People looking to advance and improve themselves through a success coach

Industry/Entity Type

Life Coaching

Contact Information for Business Card

Contact information on card.
Business name on front of card
Questions on back

Font styles to use
Other font styles liked:
• Century Gothic or other Serif style fonts that look similar to Century Gothic

Colors

Designer to choose colors to be used in the design.

Requirements
Must have
• Logo on front of card
• Business name - The Steady Forge
• Contact name - Ted Harlow
• Address - Box 4619, Littleton, CO 80127-4619
• Phone number - 303-555-0147
• Email address - harlow.ted@thesteadyforge.example
• Certifications - CSC, CCHt, PTT, PNLP
• Back of card
• Three questions on the back of the card:
• If you were at your best, what would you do right now?
• What is the decision you have been avoiding?
• What's one action you could take in the next 10 minutes?
Nice to have
• I would like to see a solid color on the front of the card that compliments the logo.
• Back should be white, or could be contrasting, but need to have the three questions.

```html
<!DOCTYPE html>
<html lang="en">
<head>
<meta charset="utf-8">
<title>The Steady Forge – Business Card</title>
<link rel="stylesheet" href="https://fonts.googleapis.com/css2?family=Open+Sans:wght@400;600;700&family=Roboto:wght@400;500;700&display=swap">
<style>
  :root {
    --navy: #1b2f66;
    --blue: #3f6db3;
    --light-blue: #8fa9d4;
    --pale-blue: #c3d1e8;
    --ink: #1d2a4d;
    --card: #ffffff;
    --backdrop: #d6d6d6;
  }
  * { box-sizing: border-box; margin: 0; padding: 0; }
  html, body { width: 1200px; height: 852px; overflow: hidden; }
  body {
    background: var(--backdrop);
    position: relative;
    font-family: "Roboto", Arial, sans-serif;
    color: var(--ink);
  }
  .card {
    position: absolute;
    width: 520px;
    height: 300px;
    background: var(--card);
    border-radius: 14px;
    overflow: hidden;
    box-shadow: 0 6px 18px rgba(0,0,0,0.18);
  }
  .card--questions { left: 90px; top: 120px; }
  .card--contact { left: 590px; top: 430px; }

  .brand {
    display: flex;
    flex-direction: column;
    align-items: center;
    font-family: "Open Sans", Arial, sans-serif;
  }
  .brand__mark {
    width: 14px; height: 14px;
    background: var(--navy);
    border-radius: 50%;
    margin-bottom: 6px;
  }
  .brand__name {
    font-weight: 700;
    color: var(--navy);
    line-height: 1.05;
    white-space: nowrap;
  }
  .brand-line {
    font-family: "Open Sans", Arial, sans-serif;
    color: var(--light-blue);
    line-height: 1.2;
    white-space: nowrap;
    margin-top: 4px;
  }

  /* Questions side */
  .card--questions .brand { position: absolute; left: 0; right: 0; top: 44px; }
  .card--questions .brand__name { font-size: 34px; }
  .card--questions .brand-line { font-size: 17px; }
  .divider {
    position: absolute;
    left: 150px; right: 40px; top: 160px;
    height: 1px;
    background: var(--pale-blue);
  }
  .questions {
    position: absolute;
    left: 0; right: 0; top: 176px;
    text-align: center;
    font-size: 15px;
    line-height: 1.45;
    color: var(--ink);
  }
  .questions .question--accent { color: var(--blue); }
  .edge-band {
    position: absolute;
    left: 0; right: 0; bottom: 0;
    height: 10px;
    display: flex;
  }
  .edge-band span { flex: 1; }
  .edge-band .band--navy { background: var(--navy); }
  .edge-band .band--blue { background: var(--blue); }
  .edge-band .band--light { background: var(--light-blue); }

  /* Contact side */
  .person { position: absolute; left: 40px; top: 50px; }
  .person__name { font-size: 24px; font-weight: 700; color: var(--navy); }
  .person__creds { font-size: 14px; color: var(--blue); margin-top: 2px; }
  .card--contact .brand { position: absolute; right: 34px; top: 70px; }
  .card--contact .brand__name { font-size: 26px; }
  .card--contact .brand-line { font-size: 14px; color: var(--blue); }
  .contact {
    position: absolute;
    left: 40px; bottom: 30px;
    font-size: 15px;
    line-height: 1.55;
    list-style: none;
  }
  .contact li { display: flex; align-items: center; gap: 9px; }
  .contact svg { width: 14px; height: 14px; fill: var(--navy); flex: none; }
</style>
</head>
<body>

<section class="card card--questions" aria-label="Card back with questions">
  <div class="brand">
    <span class="brand__mark"></span>
    <span class="brand__name">The Steady Forge</span>
    <span class="brand-line">Coaching for lasting growth</span>
  </div>
  <div class="divider"></div>
  <div class="questions">
    <p>If you were at your best, what would you do right now?</p>
    <p class="question--accent">What is the decision you have been avoiding?</p>
    <p>What's one action you could take in the next 10 minutes?</p>
  </div>
  <div class="edge-band">
    <span class="band--navy"></span><span class="band--blue"></span><span class="band--light"></span>
  </div>
</section>

<section class="card card--contact" aria-label="Card front with contact details">
  <div class="person">
    <h1 class="person__name">Ted Harlow</h1>
    <p class="person__creds">CSC, CCHt, PTT, PNLP</p>
  </div>
  <div class="brand">
    <span class="brand__mark"></span>
    <span class="brand__name">The Steady Forge</span>
    <span class="brand-line">Coaching for lasting growth</span>
  </div>
  <ul class="contact">
    <li>Box 4619, Littleton, CO 80127-4619</li>
    <li>
      <svg viewBox="0 0 16 16" aria-hidden="true"><path d="M3 1h3l1.5 4-2 1.3a8 8 0 0 0 4.2 4.2L11 8.5l4 1.5v3a2 2 0 0 1-2 2A12 12 0 0 1 1 3a2 2 0 0 1 2-2z"/></svg>
      303-555-0147
    </li>
    <li>
      <svg viewBox="0 0 16 16" aria-hidden="true"><path d="M8 1a7 7 0 1 0 0 14A7 7 0 0 0 8 1zm0 1.5c.8 0 1.8 1.6 2.1 4.3H5.9C6.2 4.1 7.2 2.5 8 2.5zM2.6 8.2h2.1c0 1.1.2 2.2.5 3.1a5.5 5.5 0 0 1-2.6-3.1zm2.1-1.4H2.6a5.5 5.5 0 0 1 2.6-3.1c-.3.9-.5 2-.5 3.1zM8 13.5c-.8 0-1.8-1.6-2.1-4.3h4.2c-.3 2.7-1.3 4.3-2.1 4.3zm2.8-2.2c.3-.9.5-2 .5-3.1h2.1a5.5 5.5 0 0 1-2.6 3.1zm.5-4.5c0-1.1-.2-2.2-.5-3.1a5.5 5.5 0 0 1 2.6 3.1z"/></svg>
      www.thesteadyforge.example
    </li>
    <li>
      <svg viewBox="0 0 16 16" aria-hidden="true"><path d="M1 3h14v10H1zm1.5 1.5v.3L8 8.7l5.5-3.9v-.3zm0 2.1v4.9h11V6.6L8 10.5z"/></svg>
      harlow.ted@thesteadyforge.example
    </li>
  </ul>
</section>

</body>
</html>
```